Business Card Design needed for logo design project

Our 2-sided business card needs to include the information sent to the awarded winner.
Updates

Reason: So sorry for the delay. Many pressing deadlines in this week.

Target Market(s)

Families of children with special needs and medical colleagues.

Industry/Entity Type

Business

Requirements
Must have
• Include logo and pertinent information.

```html
<!DOCTYPE html>
<html lang="en">
<head>
<meta charset="utf-8">
<title>Bright Pathways – Business Card</title>
<link rel="stylesheet" href="https://fonts.googleapis.com/css2?family=Arimo:wght@400;500;700&display=swap">
<style>
  :root {
    --page: #ffffff;
    --sun: #fcd22e;
    --coral: #fb6443;
    --sky: #47c6e8;
    --leaf: #6cc04a;
    --ink-light: #ffffff;
    --edge: #d9d9d9;
  }
  * { box-sizing: border-box; margin: 0; padding: 0; }
  html, body {
    width: 943px;
    height: 1200px;
    overflow: hidden;
    background: var(--page);
    font-family: "Arimo", Arial, sans-serif;
  }
  .sheet {
    position: relative;
    width: 943px;
    height: 1200px;
  }
  .card {
    position: absolute;
    left: 99px;
    width: 749px;
    height: 458px;
    overflow: hidden;
  }
  .card--front {
    top: 124px;
    background: var(--sun);
  }
  .card--back {
    top: 617px;
    height: 456px;
    background: var(--page);
    border: 1px solid var(--edge);
    box-shadow: 6px 6px 8px rgba(0, 0, 0, 0.35);
  }
  .front-decoration {
    position: absolute;
    inset: 0;
    background:
      radial-gradient(ellipse 70% 55% at 40% 30%, rgba(251, 100, 67, 0.45), rgba(251, 100, 67, 0) 70%),
      radial-gradient(ellipse 45% 50% at 88% 55%, rgba(71, 198, 232, 0.45), rgba(71, 198, 232, 0) 70%);
  }
  .contact {
    position: absolute;
    left: 180px;
    top: 220px;
    color: var(--ink-light);
    font-size: 26px;
    line-height: 32px;
    font-weight: 500;
  }
  .contact__address { margin-top: 8px; }
  .contact__web {
    margin-top: 8px;
    color: var(--leaf);
    font-weight: 700;
    font-size: 25px;
  }
  .brand {
    position: absolute;
    left: 0;
    right: 0;
    top: 158px;
    display: flex;
    align-items: center;
    justify-content: center;
    gap: 14px;
  }
  .brand__dot {
    width: 34px;
    height: 34px;
    border-radius: 50%;
    background: var(--leaf);
  }
  .brand__name {
    font-size: 52px;
    font-weight: 700;
    color: var(--coral);
    letter-spacing: 0.5px;
  }
  .tagline {
    position: absolute;
    left: 0;
    right: 0;
    top: 344px;
    text-align: center;
    font-weight: 700;
  }
  .tagline__service {
    font-size: 26px;
    color: var(--coral);
    line-height: 30px;
    letter-spacing: 0.3px;
  }
  .tagline__motto {
    font-size: 18px;
    color: var(--sky);
    line-height: 22px;
  }
</style>
</head>
<body>
  <main class="sheet">
    <section class="card card--front">
      <div class="front-decoration" role="img" aria-label="Sweeping coral and sky-blue arches across the yellow card"></div>
      <div class="contact">
        <p class="contact__name">Daniel Hart CEO</p>
        <p class="contact__phone">Tel. 03 9100 4821</p>
        <p class="contact__email">Email dh@kitemail.com.au</p>
        <p class="contact__address">48 Larchfield Road<br>Ferndale Vic 3790</p>
        <p class="contact__web">www.brightpathways.com.au</p>
      </div>
    </section>

    <section class="card card--back">
      <div class="brand">
        <span class="brand__dot"></span>
        <span class="brand__name">Bright Pathways</span>
      </div>
      <div class="tagline">
        <p class="tagline__service">Pediatric Therapy Services</p>
        <p class="tagline__motto">Guiding little steps · Growing together</p>
      </div>
    </section>
  </main>
</body>
</html>
```